Business Card Design

this is a new company aimed at the automotive glass industry
what we do is repair cracked windscreens its based in western austraila
I like the old dragracing signwritting logos
I want it to stand out thats why ive gone with the name and title
I dont have a logo but if you can think of one that would be great
but not essential
on the back of the business card i would like Quicker Cheaper Better

Target Market(s)

automotive (car yards ,car auctions , trucking companys ect )

Industry/Entity Type

Automotive

Contact Information for Business Card

Pane Rangers ,
Glass Crack repair specialists ,
Darren Whitlock ,0438 162 705 ,dwhitlock@paneriderswa.com.au

```html
<!DOCTYPE html>
<html lang="en">
<head>
<meta charset="utf-8">
<title>Pane Rangers – Business Card</title>
<link href="https://fonts.googleapis.com/css2?family=Open+Sans:wght@400;600;700&display=swap" rel="stylesheet">
<style>
  :root{
    --bg:#e9e6e1;
    --card:#141416;
    --pink:#e8336b;
    --purple:#8a3fa8;
    --white:#f4f4f6;
    --grey:#b9b9c0;
  }
  *{margin:0;padding:0;box-sizing:border-box}
  html,body{width:1200px;height:1023px;overflow:hidden}
  body{background:var(--bg);font-family:"Open Sans",Arial,sans-serif;position:relative}
  .card{position:absolute;left:220px;width:760px;height:463px;background:var(--card);
        border-radius:6px;overflow:hidden;box-shadow:0 6px 18px rgba(0,0,0,.25)}
  .card--front{top:40px}
  .card--back{top:520px;background:radial-gradient(circle at 62% 55%,#26262c 0%,var(--card) 60%)}

  .brand-name,.brand-tagline,.contact,.person,.slogan{white-space:nowrap}

  /* front */
  .front-photo{position:absolute;left:0;top:0;width:760px;height:463px}
  .brand-name{position:absolute;font-weight:700;color:var(--pink);text-transform:uppercase;letter-spacing:1px;line-height:1}
  .card--front .brand-name{left:28px;top:150px;font-size:38px}
  .brand-tagline{position:absolute;color:var(--white);text-transform:uppercase;font-weight:600;letter-spacing:1.5px}
  .card--front .brand-tagline{left:30px;top:198px;font-size:12px}
  .contact{position:absolute;left:478px;top:60px;padding-left:16px;border-left:2px solid var(--pink);
           color:var(--white);font-size:15px;line-height:30px}
  .person{position:absolute;left:430px;top:330px}
  .person__name{color:var(--pink);font-weight:700;font-size:26px;text-transform:uppercase;letter-spacing:1px;line-height:1.2}
  .person__role{color:var(--grey);font-size:17px;margin-top:4px}

  /* back */
  .back-emblem{position:absolute;left:330px;top:90px;width:300px;height:300px;border-radius:50%;
               background:radial-gradient(circle,rgba(220,220,230,.28) 0%,rgba(120,120,130,.12) 45%,rgba(0,0,0,0) 72%)}
  .card--back .brand-name{left:70px;top:140px;font-size:72px}
  .card--back .brand-tagline{left:74px;top:232px;font-size:16px}
  .slogan{position:absolute;left:74px;top:330px;color:var(--white);font-weight:700;font-size:19px;letter-spacing:2.5px}
  .slogan__dot{display:inline-block;width:7px;height:7px;border-radius:50%;background:var(--pink);margin:0 12px;vertical-align:middle}
</style>
</head>
<body>

<section class="card card--front">
  <svg class="front-photo" viewBox="0 0 760 463" role="img" aria-label="Photo of a cracked windscreen with a star chip against a blue sky">
    <defs>
      <linearGradient id="photoTone" x1="0" y1="0" x2="1" y2="1">
        <stop offset="0" stop-color="#1f8fb8"/>
        <stop offset=".45" stop-color="#2ab0c8"/>
        <stop offset=".8" stop-color="#3d6a58"/>
        <stop offset="1" stop-color="#2a2f2a"/>
      </linearGradient>
      <linearGradient id="bandTone" x1="0" y1="1" x2="1" y2="0">
        <stop offset="0" stop-color="#e8336b"/>
        <stop offset="1" stop-color="#8a3fa8"/>
      </linearGradient>
    </defs>
    <path d="M0 0 H480 Q420 330 0 440 Z" fill="url(#photoTone)"/>
    <path d="M480 0 Q420 330 0 440" fill="none" stroke="url(#bandTone)" stroke-width="9"/>
  </svg>
  <div class="brand-name">Pane Rangers</div>
  <div class="brand-tagline">Glass crack repair specialists</div>

  <div class="contact">
    <div>0438 162 705</div>
    <div>dwhitlock@paneriderswa.com.au</div>
    <div>www.paneriderswa.com.au</div>
  </div>
  <div class="person">
    <div class="person__name">Darren Whitlock</div>
    <div class="person__role">Owner | Glass repair technician</div>
  </div>
</section>

<section class="card card--back">
  <div class="back-emblem" role="img" aria-label="Decorative radiating shattered-glass pattern"></div>
  <div class="brand-name">Pane Rangers</div>
  <div class="brand-tagline">Glass crack repair specialists</div>
  <div class="slogan">QUICKER<span class="slogan__dot"></span>CHEAPER<span class="slogan__dot"></span>BETTER</div>
</section>

</body>
</html>
```